stichtinglumo . Eu

With its head office in Amsterdam stichtinglumo.eu we will have offices in the Netherlands, Luxembourg , Belgium, switzerland, Monaco, Liechtenstein and we want pictures of those countries .
UVO.CA a popular Canadian non profit is opening in the Europe and will require a website that appeals those countries we specified.
Please focus on reuse of electronics. Mention ‘WEEE’
Donations to charities, non profit, school and orphanage.
Donates to 3rd world countries like Madagascar
Industry
Technology
Color Preferences
green and blue and similar to uvo.ca
Our Ideas & Additional Information
uvo.ca logo
use these websites as examples to copy and make similar websites
www.bzl.mg
www.uvo.ca
www.tastavorlinka.ba
stichtinglumo.eu - non profit , foundation , association
Target Market(s)
Amsterdam
Industry/Entity Type
Technology, nonprofit
Number of Pages Required
1 page

```html
<!DOCTYPE html>
<html lang="mg">
<head>
<meta charset="utf-8">
<title>Stichting LUMO – Manomeza Anio</title>
<link href="https://fonts.googleapis.com/css2?family=Poppins:wght@300;400;500;600;700&display=swap" rel="stylesheet">
<style>
:root{
  --green:#62b862;
  --green-dark:#4fa34f;
  --blue:#0a4fa6;
  --blue-deep:#0d4ea3;
  --ink:#111;
  --muted:#444;
  --pale:#eaf0f5;
  --white:#fff;
}
*{box-sizing:border-box;margin:0;padding:0}
html,body{width:1200px;height:3412px;overflow:hidden}
body{font-family:'Poppins',sans-serif;color:var(--ink);background:var(--white);position:relative}
.abs{position:absolute}
.btn{position:absolute;display:flex;align-items:center;justify-content:center;border-radius:22px;color:#fff;font-weight:600;font-size:13px;text-decoration:none}
.btn-green{background:var(--green)}
.btn-blue{background:var(--blue)}

/* header */
.site-header{position:absolute;left:0;top:0;width:1200px;height:95px;background:#fff;z-index:5}
.brand{position:absolute;left:100px;top:8px;width:118px;height:118px;border-radius:50%;background:#fff;display:flex;align-items:center;justify-content:center;z-index:6}
.brand span{font-weight:700;font-size:28px;color:var(--green)}
.nav{position:absolute;top:38px;left:290px;display:flex;gap:28px;font-size:13px}
.nav a{color:#222;text-decoration:none}
.header-cta{left:910px;top:26px;width:183px;height:42px}

/* hero */
.hero{position:absolute;left:0;top:95px;width:1200px;height:620px}
.hero-photo{position:absolute;inset:0;background:linear-gradient(100deg,#5a3a22 0%,#8a5a34 40%,#3c4c9a 65%,#6b4a30 100%)}
.hero-shade{position:absolute;inset:0;background:linear-gradient(90deg,rgba(40,25,15,.55),rgba(40,25,15,0) 55%)}
.hero h1{position:absolute;left:105px;top:80px;width:420px;color:#fff;font-size:37px;line-height:50px;font-weight:700}
.hero p{position:absolute;left:105px;top:292px;width:400px;color:#fff;font-size:14px;line-height:20px}
.hero .b1{left:105px;top:354px;width:141px;height:41px}
.hero .b2{left:262px;top:354px;width:226px;height:41px}
.badge{position:absolute;top:422px;width:82px;height:82px;border-radius:50%;border:4px solid #fff}
.hero-curve{position:absolute;left:0;bottom:-2px}
.scroll-dot{position:absolute;left:552px;top:662px;width:96px;height:96px;border-radius:50%;background:#fff;box-shadow:0 8px 20px rgba(0,0,0,.08);display:flex;align-items:center;justify-content:center}

/* steps */
.section-title{position:absolute;left:0;width:1200px;text-align:center;font-weight:500;font-size:32px}
.step{position:absolute;width:240px;text-align:center}
.step .ring{width:106px;height:106px;border-radius:50%;border:1px solid #ddd;margin:0 auto;position:relative;display:flex;align-items:center;justify-content:center;background:#fff}
.step .num{position:absolute;left:-4px;top:0;width:24px;height:24px;border-radius:50%;background:var(--green);color:#fff;font-size:11px;display:flex;align-items:center;justify-content:center}
.step h3{font-size:14px;font-weight:500;margin-top:14px}
.step p{font-size:12px;line-height:18px;color:var(--muted);margin-top:2px}
.step-arrow{position:absolute;top:904px;color:#bbb;font-size:18px}

/* countries */
.band-pale{position:absolute;left:0;width:1200px;background:var(--pale)}
.countries h2{position:absolute;left:143px;top:1268px;font-size:32px;font-weight:500;line-height:39px}
.country{position:absolute;font-size:15px;display:flex;align-items:center;gap:8px}
.map{position:absolute;left:619px;top:1238px;width:440px;height:352px;border-radius:20px;background:linear-gradient(135deg,#7fcfe0 0%,#a9dcb0 35%,#b9e3b4 60%,#8fd0dc 100%);overflow:hidden}
.map-card{position:absolute;left:90px;top:175px;width:188px;height:88px;background:#fff;padding:12px 16px}
.map-card b{font-size:16px;font-weight:500;display:block}
.map-card small{font-size:10px;line-height:14px;display:block;margin-top:4px;color:#333}
.map-pin{position:absolute}

/* stats */
.stat{position:absolute;width:300px;height:300px;border-radius:50%;display:flex;flex-direction:column;align-items:center;justify-content:center;text-align:center}
.stat.dashed{border:2px dashed var(--blue)}
.stat.solid{background:var(--green);color:#fff}
.stat strong{font-size:38px;font-weight:600;color:var(--blue)}
.stat.solid strong{color:#fff}
.stat span{font-size:19px;line-height:24px;font-weight:400}

/* weee */
.weee-photo{position:absolute;left:141px;top:2320px;width:440px;height:353px;border-radius:18px;background:linear-gradient(135deg,#d9d6d0,#a8865e 55%,#4b3b2a)}
.weee h2{position:absolute;left:644px;top:2338px;font-size:34px;font-weight:500;line-height:42px;width:420px}
.weee p{position:absolute;left:645px;top:2476px;width:400px;font-size:13px;line-height:22px;color:#333}
.weee .btn{left:645px;top:2605px;width:227px;height:42px}

/* donate */
.donate{position:absolute;left:0;top:2763px;width:1200px;height:322px;background:linear-gradient(90deg,#5aa95c,#6fbf63 50%,#5aaa5a)}
.donate-col{position:absolute;top:95px;width:440px;color:#fff}
.donate-col h2{font-size:33px;font-weight:500}
.donate-col p{font-size:12px;line-height:23px;margin-top:8px}
.donate-col .btn{position:relative;width:134px;height:42px;margin-top:28px}

/* footer */
.site-footer{position:absolute;left:0;top:3085px;width:1200px;height:327px;background:var(--blue-deep);color:#fff}
.foot-brand{position:absolute;left:552px;top:30px;width:96px;height:96px;border-radius:50%;border:2px solid rgba(255,255,255,.5);display:flex;align-items:center;justify-content:center;font-weight:700;font-size:26px}
.foot-nav{position:absolute;top:152px;left:0;width:1200px;display:flex;justify-content:center;gap:28px;font-size:13px}
.contact{position:absolute;top:202px;display:flex;align-items:center;gap:14px}
.contact .ic{width:42px;height:42px;border-radius:50%;border:1px solid rgba(255,255,255,.6);display:flex;align-items:center;justify-content:center}
.contact b{display:block;font-size:12px;font-weight:600;letter-spacing:.5px}
.contact span{font-size:13px}
.vsep{position:absolute;top:208px;width:1px;height:30px;background:rgba(255,255,255,.25)}
.foot-line{position:absolute;left:141px;top:275px;width:918px;height:1px;background:rgba(255,255,255,.25)}
.foot-copy{position:absolute;top:298px;font-size:12px}
</style>
</head>
<body>

<header class="site-header">
  <div class="brand"><span>BZL</span></div>
  <nav class="nav">
    <a>An-trano</a><a>About</a><a>Manomeza</a><a>WEEE Recycling</a><a>Tany</a><a>Fiantraikany</a><a>Contact</a>
  </nav>
  <a class="btn btn-green header-cta">Manome Electronics</a>
</header>

<section class="hero">
  <div class="hero-photo" role="img" aria-label="Ankizy roa mampiasa solosaina ao an-dakilasy"></div>
  <div class="hero-shade"></div>
  <h1>Omeo Fiainana Fanindroany Ny Elektrônikao – Manomeza Anio!</h1>
  <p>Manohana Sekoly, Asa Fanasoavana &amp; Vondrom piarahamonina Manerana an'i Eoropa &amp; Ambony</p>
  <a class="btn btn-green b1">Manome Izao</a>
  <a class="btn btn-blue b2">Mianara Momba Ny WEEE</a>
  <div class="badge" style="left:105px;background:#fff"></div>
  <div class="badge" style="left:194px;background:#2e8b3c"></div>
  <svg class="hero-curve" width="1200" height="130" viewBox="0 0 1200 130">
    <path d="M0 30 Q300 120 700 100 Q1000 80 1200 0 L1200 130 L0 130Z" fill="var(--blue)"/>
    <path d="M0 55 Q300 135 700 112 Q1000 95 1200 25 L1200 130 L0 130Z" fill="#fff"/>
  </svg>
</section>
<div class="scroll-dot">
  <svg width="26" height="38" viewBox="0 0 26 38"><rect x="1.5" y="1.5" width="23" height="35" rx="11.5" fill="none" stroke="var(--green)" stroke-width="2"/><path d="M9 16l4 4 4-4M9 21l4 4 4-4" fill="none" stroke="var(--green)" stroke-width="1.6"/></svg>
</div>

<h2 class="section-title" style="top:792px">Ahoana No Fiasan'ny Fanomezanao</h2>

<div class="step" style="left:185px;top:860px">
  <div class="ring"><span class="num">01</span>
    <svg width="50" height="46" viewBox="0 0 50 46" fill="none" stroke="var(--blue)" stroke-width="2"><rect x="8" y="10" width="34" height="32" rx="3"/><path d="M4 10h42M18 4h14v6"/><path d="M20 28l5-7 5 7z"/></svg>
  </div>
  <h3>Manangona</h3>
  <p>Manomàna famandrihana na fanaterana elektronika any amin'ny biraonay.</p>
</div>
<div class="step-arrow" style="left:442px">→</div>
<div class="step" style="left:480px;top:860px">
  <div class="ring"><span class="num">02</span>
    <svg width="50" height="46" viewBox="0 0 50 46" fill="none" stroke="var(--blue)" stroke-width="2"><rect x="4" y="4" width="42" height="28" rx="2"/><path d="M25 32v8M15 42h20"/><path d="M18 14a8 8 0 0 1 14 0M32 22a8 8 0 0 1-14 0M30 11l2 3-3 1M20 25l-2-3 3-1"/></svg>
  </div>
  <h3>Fanavaozana</h3>
  <p>Manamboatra sy manao fitiliana fitaovana izahay mba hampiasaina indray.</p>
</div>
<div class="step-arrow" style="left:738px">→</div>
<div class="step" style="left:777px;top:860px">
  <div class="ring"><span class="num">03</span>
    <svg width="54" height="50" viewBox="0 0 54 50" fill="none" stroke="var(--blue)" stroke-width="2"><path d="M8 24l19-9 19 9-19 9z M8 24v14l19 9 19-9V24M27 33v14"/><path d="M27 20c-6-4-8-9-4-11 2-1 4 0 4 2 0-2 2-3 4-2 4 2 2 7-4 11z"/><path d="M27 2v4M18 5l2 3M36 5l-2 3"/></svg>
  </div>
  <h3>Manomeza</h3>
  <p>Nalefa tany an-tsekoly, ONG, ary Madagasikara.</p>
</div>

<div class="band-pale" style="top:1145px;height:535px"></div>
<section class="countries">
  <h2>Manitatra Manerana<br>An'i Eoropa</h2>
  <div class="country" style="left:143px;top:1370px"><svg width="12" height="16" viewBox="0 0 12 16"><path d="M6 0a6 6 0 0 0-6 6c0 4.5 6 10 6 10s6-5.5 6-10a6 6 0 0 0-6-6z" fill="var(--green)"/><circle cx="6" cy="6" r="2.2" fill="#fff"/></svg>Pays-Bas</div>
  <div class="country" style="left:285px;top:1370px"><svg width="12" height="16" viewBox="0 0 12 16"><path d="M6 0a6 6 0 0 0-6 6c0 4.5 6 10 6 10s6-5.5 6-10a6 6 0 0 0-6-6z" fill="var(--green)"/><circle cx="6" cy="6" r="2.2" fill="#fff"/></svg>Luxembourg</div>
  <div class="country" style="left:143px;top:1415px"><svg width="12" height="16" viewBox="0 0 12 16"><path d="M6 0a6 6 0 0 0-6 6c0 4.5 6 10 6 10s6-5.5 6-10a6 6 0 0 0-6-6z" fill="var(--green)"/><circle cx="6" cy="6" r="2.2" fill="#fff"/></svg>Belzika</div>
  <div class="country" style="left:285px;top:1415px"><svg width="12" height="16" viewBox="0 0 12 16"><path d="M6 0a6 6 0 0 0-6 6c0 4.5 6 10 6 10s6-5.5 6-10a6 6 0 0 0-6-6z" fill="var(--blue)"/><circle cx="6" cy="6" r="2.2" fill="#fff"/></svg>Soisa</div>
  <div class="country" style="left:143px;top:1460px"><svg width="12" height="16" viewBox="0 0 12 16"><path d="M6 0a6 6 0 0 0-6 6c0 4.5 6 10 6 10s6-5.5 6-10a6 6 0 0 0-6-6z" fill="var(--green)"/><circle cx="6" cy="6" r="2.2" fill="#fff"/></svg>Monaco</div>
  <div class="country" style="left:285px;top:1460px"><svg width="12" height="16" viewBox="0 0 12 16"><path d="M6 0a6 6 0 0 0-6 6c0 4.5 6 10 6 10s6-5.5 6-10a6 6 0 0 0-6-6z" fill="var(--green)"/><circle cx="6" cy="6" r="2.2" fill="#fff"/></svg>Liechtenstein</div>
  <a class="btn btn-blue" style="left:141px;top:1513px;width:183px;height:42px">Mifandraisa Aminay</a>
  <div class="map" role="img" aria-label="Sarintany an'i Eoropa misy ireo firenena iasana">
    <div class="map-card"><b>Soisa</b><small>123 Ut wisi enim ad minim veniam quis nostrud.</small></div>
  </div>
</section>

<h2 class="section-title" style="top:1760px">Ny Fiantraikantsika Amin'ny Nomery</h2>
<div class="stat dashed" style="left:179px;top:1838px"><strong>50000</strong><span>Fitaovana ampiasaina<br>indray</span></div>
<div class="stat dashed" style="left:720px;top:1838px"><strong>100</strong><span>Sekoly tohanana</span></div>
<div class="stat solid" style="left:450px;top:1838px"><strong>200</strong><span>Taoniny amin'ny<br>E-Fako Recycle</span></div>

<div class="band-pale" style="top:2228px;height:535px"></div>
<section class="weee">
  <div class="weee-photo" role="img" aria-label="Boaty feno fitendry sy tariby elektronika ho averina ampiasaina"></div>
  <h2>Responsible Electronics Recycling (WEEE)</h2>
  <p>Ny Stichting LUMO dia manaraka ny fitsipiky ny EU WEEE, izay miantoka ny fanodinana ny fitaovana elektronika rehetra na havaozina araka ny tokony ho izy. Ny fanomezanao dia manampy amin'ny fampihenana ny e-fako ary manohana ny fampandrosoana maharitra.</p>
  <a class="btn btn-blue">Hamantatra Bebe Kokoa</a>
</section>

<section class="donate" role="img" aria-label="Ankizy mianatra ao an-dakilasy, voasarona loko maitso">
  <div class="donate-col" style="left:141px">
    <h2>Manome Fitaovana</h2>
    <p>Manaiky solosaina finday, finday, tablette ary maro hafa izahay. Mialà any amin'ny biraonay na mandamina ny fakana.</p>
    <a class="btn btn-blue">Manome izao</a>
  </div>
  <div class="donate-col" style="left:648px">
    <h2>Tohano ara-bola</h2>
    <p>Ny fandraisanao anjara dia manampy anay hanavao ny fitaovana sy hahatratra vondrom-piarahamonina maro kokoa.</p>
    <a class="btn btn-blue">Manome vola</a>
  </div>
</section>

<footer class="site-footer">
  <div class="foot-brand">BZL</div>
  <nav class="foot-nav"><span>An-trano</span><span>About</span><span>Manomeza</span><span>WEEE Recycling</span><span>Tany</span><span>Fiantraikany</span><span>Contact</span></nav>
  <div class="contact" style="left:187px"><div class="ic"><svg width="18" height="14" viewBox="0 0 18 14" fill="none" stroke="#fff" stroke-width="1.5"><rect x="1" y="1" width="16" height="12" rx="1"/><path d="M1 2l8 6 8-6"/></svg></div><div><b>EMAIL</b><span>info@stichtinglumo.eu</span></div></div>
  <div class="vsep" style="left:412px"></div>
  <div class="contact" style="left:447px"><div class="ic"><svg width="14" height="18" viewBox="0 0 12 16"><path d="M6 0a6 6 0 0 0-6 6c0 4.5 6 10 6 10s6-5.5 6-10a6 6 0 0 0-6-6z" fill="#fff"/><circle cx="6" cy="6" r="2.2" fill="var(--blue-deep)"/></svg></div><div><b>ADDRESS</b><span>Stichting LUMO Amsterdam, Netherlands</span></div></div>
  <div class="vsep" style="left:787px"></div>
  <div class="contact" style="left:824px"><div class="ic"><svg width="18" height="18" viewBox="0 0 24 24" fill="#fff"><path d="M6.6 10.8a15 15 0 0 0 6.6 6.6l2.2-2.2c.3-.3.7-.4 1-.2 1.1.4 2.3.6 3.6.6.6 0 1 .4 1 1V20c0 .6-.4 1-1 1A17 17 0 0 1 3 4c0-.6.4-1 1-1h3.5c.6 0 1 .4 1 1 0 1.3.2 2.5.6 3.6.1.3 0 .7-.2 1z"/></svg></div><div><b>TELEFAONINA</b><span>+31 100 200 300</span></div></div>
  <div class="foot-line"></div>
  <div class="foot-copy" style="left:141px">© 2025 BZL. Zo rehetra voatokana.</div>
  <div class="foot-copy" style="left:796px">Politika manokana &nbsp; | &nbsp; Fepetra fampiasana</div>
</footer>

</body>
</html>
```